vermalo web design

- Company / Site Description
We are developing a website that will allow anyone in Europe to find in one click, cultural things to do (Exhibition, Museum, Monument, Zoo, Aquarium, Archaeological site…) with friends or family, and to organize the visit (book a ticket / a private visit, book a restaurant nearby…).

Examples
1. You're in London with your girlfriend, it's saturday 10 am, you have two hours to spend and you want to see an exhibition. We provide you in one click all the exhibition matching your location / time and date.

2. You're in Berlin with some friends, it's thursday night you want to go out, but you don't know what to do. We provide you a list of experience, you can select for instance "I want to be on top of the world", and we show you a list of venues matching the selected experience / date / time /location of your request.

- Brand name : Vermalo
- Activity : Cultural Leisure, cultural entertainment

- Target audience
Broad target will be between 20 and 55. Core target will be between 25 and 40. Most likely to live in a city and in Europe.

- Behaviours and preferences
Our user is under time constraint (few minutes to find and choose his visit), idea constraint (is not sure about what to do and see) and money constraint.
He wants to have an easy to use website, not cluttered with information, focussed on added value information. He wants to have a website which is modern, fun and elegant that he will deem as professional and trustworthy.

- Our expectations (Do’s and Don’t)
We want to move away from traditional design. We want some OUT OF THE BOX design. Think of a website design that will look like an app design.
We want to make an awesome / extra ordinary /remember-able design. The design must be so cool, that the user wants to come back to the site. In two words: THINK EXTRAORDINARY.
You can use photos to help the user understand functions. If you use photo, use creative commons license photo.
Avoid black colors

- Functional Requirements
We need Four pages:
1. Home Page (desktop and mobile version): it’s both the homepage and the assistant page. This page will allow the user to find in one click his visit (please refer to the pdf file Assistant home page). The page must be self-explanatory for a first time user.
2. Assistant result page (desktop version): it’s the page that display the results found by the assistant based on the criteria search (please refer to the pdf file mockup - Assistant result page)
3. Site / Event page (desktop version): it’s the page that display each result information (please refer to the pdf file mockup – Event / Site Page)
The pdf files list all the elements include in each page + gives you a mockup of each page (just to put in perspective the element required). You are completely free about the design.
We don’t have the logo yet. Use a dummy logo for your page design.
The selected winner can expect to work with us immediately after the contest and on a on a regular basis later on.

- Technical Requirements
No Flash
For the winner, we will manage the CSS you will just need to provide :
. One PSD file containing all the pages
. Inside the PSD file we want for each page two groups: the first group will embed the desktop design, the second group will embed the responsive mobile design (Home Page only).
In total there should be 4 groups inside the PSD file (3 desktop groups, 1 mobile group).
Each group must contain all the elements specified in the pdf file

Website we like
http://demo.plandorix.example/?theme=Velunt
http://rosabel.quintorhub.example/#home
http://blogsite.fenk.daltoroute.example/2/
http://demo.plandorix.example/?theme=Mosaru
http://www.quarnivo.example/themes/lumbe/
http://gridmarket.example/item/tav-responsive-photography-blog-theme/full_screen_preview/8146027
http://items.zkvortel.example/?product=example
http://uk.harnoway.example

Reason: Due to the request of several designers, we have agreed to add 7 additional days to the contest deadline. Thank you. The vermalo team

Reason: We still need to collect all the votes. Sorry for the delay.

Reason: Hello, We extend the contest deadline, in order to collect all the votes from the poll. We should have everything finalized by sunday. Thank you vermalo team

```html
<!DOCTYPE html>
<html lang="en">
<head>
<meta charset="UTF-8">
<title>Vermalo – Find cultural visits in one click</title>
<link rel="stylesheet" href="https://fonts.googleapis.com/css2?family=Archivo+Black&family=Arimo:wght@400;700&display=swap">
<style>
  :root {
    --navy: #0d1575;
    --ink-purple: #3d1a73;
    --hero-blue: #0a1e8c;
    --hero-blue-light: #2447a8;
    --hero-blue-deep: #061470;
    --white: #ffffff;
  }
  * { box-sizing: border-box; margin: 0; padding: 0; }
  html, body { width: 1200px; height: 755px; overflow: hidden; background: var(--white); }
  body { font-family: "Arimo", Arial, sans-serif; color: var(--navy); }

  .page { position: relative; width: 1200px; height: 755px; overflow: hidden; }

  /* Left sidebar */
  .sidebar { position: absolute; left: 0; top: 0; width: 415px; height: 755px; background: var(--white); }
  .brand { position: absolute; left: 36px; top: 18px; font-size: 30px; font-weight: 400; color: var(--navy); letter-spacing: 1px; }
  .intro-title { position: absolute; left: 40px; top: 194px; font-size: 19px; font-weight: 700; line-height: 23px; color: var(--ink-purple); }
  .intro-text { position: absolute; left: 40px; top: 285px; font-size: 17px; line-height: 23px; color: var(--ink-purple); }

  .criteria { position: absolute; left: 35px; top: 449px; list-style: none; }
  .criteria-field {
    width: 293px; height: 42px; margin-bottom: 24px;
    border: 1px solid var(--navy); border-radius: 21px;
    padding-left: 18px; display: flex; align-items: center;
    font-size: 19px; color: #1a1a40;
  }
  .criteria-field:nth-child(2) { margin-bottom: 22px; }

  .language { position: absolute; left: 31px; top: 717px; font-size: 19px; color: var(--navy); }
  .language strong { font-weight: 700; }

  /* Hero */
  .hero { position: absolute; left: 415px; top: 0; width: 785px; height: 755px; }
  .hero-photo {
    position: absolute; inset: 0;
    background:
      radial-gradient(ellipse 260px 340px at 230px 300px, var(--hero-blue-light), transparent 70%),
      radial-gradient(ellipse 300px 380px at 640px 320px, var(--hero-blue-light), transparent 70%),
      linear-gradient(180deg, var(--hero-blue) 0%, var(--hero-blue) 60%, var(--hero-blue-deep) 100%);
  }

  .account { position: absolute; right: 30px; top: 24px; display: flex; align-items: center; gap: 12px; }
  .account-login { font-family: "Arimo", Arial, sans-serif; font-weight: 700; font-size: 16px; color: var(--white); letter-spacing: 0.5px; margin-left: 0; }

  .main-nav { position: absolute; left: 20px; top: 112px; display: flex; gap: 54px; }
  .main-nav a { color: var(--white); text-decoration: none; font-size: 19px; padding-bottom: 12px; }
  .main-nav a.is-active { border-bottom: 1px solid var(--white); padding-right: 6px; }

  .assistant { position: absolute; left: 193px; top: 425px; display: flex; align-items: center; gap: 8px; }
  .assistant-field {
    width: 331px; height: 62px; border-radius: 31px; background: var(--white);
    display: flex; align-items: center; justify-content: center;
    font-family: "Archivo Black", "Arial Black", sans-serif; font-size: 40px; color: var(--navy); letter-spacing: 1px;
  }
  .assistant-go {
    width: 80px; height: 60px; border: 2px solid var(--white); background: var(--hero-blue-deep);
    display: flex; align-items: center; justify-content: center;
    font-family: "Archivo Black", "Arial Black", sans-serif; font-size: 36px; color: var(--white);
  }

  .more { position: absolute; left: 650px; top: 719px; display: flex; align-items: center; gap: 8px; font-weight: 700; font-size: 16px; color: var(--white); letter-spacing: 0.5px; }
</style>
</head>
<body>
<div class="page">

  <aside class="sidebar">
    <div class="brand">Vermalo</div>

    <p class="intro-title">Find in one click<br>Exhibitions, museums,<br>monuments, zoos...</p>
    <p class="intro-text">Tell us what you like, we will<br>till you where to go !</p>

    <ul class="criteria">
      <li class="criteria-field">SATURDAY 14 SEPTEMBER</li>
      <li class="criteria-field">11 : AM</li>
      <li class="criteria-field">PARIS, France</li>
    </ul>

    <p class="language"><strong>LANGUAGE :</strong> ENGLISH</p>
  </aside>

  <main class="hero">
    <div class="hero-photo" role="img" aria-label="Photo of two tigers lying on grass, tinted deep blue"></div>

    <div class="account">
      <svg width="34" height="32" viewBox="0 0 34 32" aria-label="Search">
        <circle cx="13" cy="13" r="10.5" fill="none" stroke="#fff" stroke-width="2.5"/>
        <line x1="21" y1="21" x2="31" y2="30" stroke="#fff" stroke-width="3" stroke-linecap="round"/>
      </svg>
      <span class="account-login">LOGIN</span>
      <svg width="20" height="16" viewBox="0 0 20 16" aria-hidden="true" style="margin-left:10px">
        <polygon points="0,0 20,0 10,16" fill="#fff"/>
      </svg>
    </div>

    <nav class="main-nav">
      <a href="#" class="is-active">MY ASSISTANTS</a>
      <a href="#">MY FAVOURITES</a>
    </nav>

    <div class="assistant">
      <div class="assistant-field">YOU WANT ?</div>
      <div class="assistant-go">GO</div>
    </div>

    <div class="more">
      <span>MORE</span>
      <svg width="17" height="15" viewBox="0 0 17 15" aria-hidden="true">
        <polygon points="0,0 17,0 8.5,15" fill="#fff"/>
      </svg>
    </div>
  </main>

</div>
</body>
</html>
```